Business Card Upgrade

I have designed our business card using our new logo. I think it needs imporovements. We used to have two cards for our business. One card was for our software business, and the other was for our consulting business. We are now in the process of combining our websites, marketing, name, and a new logo.

Our goal is to have a really sharp professional logo. One reason I designed the card the way I did was that our Titles are sometimes long, and by separating the person's name and title, it shows up very well and the title can be adjusted no matter how long it is. Sometimes the title can be 4 or 5 words or more.

We really like our logo on black as it shows up very nice. Our PMS colors are as follows: 368C and 459C.

The Designer that will be working with us will need to deliver the following:

The front and back of the Business Card Design will need to be delivered in a high quality JPEG, and
The front and back of the Business Card Design in Illustrator Format .ai
Any fonts will need to be sent to us if they are not standard and are required to open the Illustrator file correctly.

To help us get a good idea of the card with a title, please use the title: " Director of Software Development "

NOTE: The chosen designer will be selected to design our new letterhead within 2 weeks from the closing of this contest.

To help us make sure the card design works with longer titles, please use the followign job title on the card:  

"Director of Software and Product Development"

 

ALL DESIGNERS:

1. I appreciate the different angles you are showing the cards, but please be sure and always show the direct view, so I can see the layout and what the person I hand the card will see.

2. Please do not use white.  Please use off white as I don't care for white cards and they get dirty easy and do not represent the designs well.

Dear Designers,

Please provide samples straight one as a viewer of the card will see.  Some of the angles that are presented make it impossible to tell how everything fits, and sometimes even makes areas look skewed. So, please provide a straight sample view.

Pinnacle 400 company executives such as Vice Presidents, and Directors

Software

• Professional looking Card.

Our customers are Directors, Vice Presidents, and Presidents of companies as large as Pinnacle 400 companies. The card needs to get attention wile still looking professional.

Delivery of the finished product in Illustrator Format with any fonts needed to edit the text or open the file.

The card will be a heavy stock with a soft touch coating for that silk feel.

```html
<!DOCTYPE html>
<html lang="en">
<head>
<meta charset="utf-8">
<title>Northgate Trade Corporation – Business Card Front and Back</title>
<link rel="stylesheet" href="https://fonts.googleapis.com/css2?family=Open+Sans:wght@400;700&family=Montserrat:wght@800&display=swap">
<style>
  :root {
    --canvas-bg: #d9d4cf;
    --card-black: #050505;
    --brand-green: #5aa33a;
    --brand-green-dark: #1f5a1c;
    --brand-gold: #d3c28e;
    --gold-light: #f1ece0;
    --gold-deep: #c9b57c;
    --ink-dark: #1b1b1b;
    --label-ring: #6cb31f;
    --label-fill: #ece9e6;
  }
  * { box-sizing: border-box; margin: 0; padding: 0; }
  html, body { width: 1200px; height: 1200px; overflow: hidden; }
  body {
    background: radial-gradient(circle at 30% 20%, #f1eeec 0%, var(--canvas-bg) 75%);
    font-family: "Open Sans", Arial, sans-serif;
    position: relative;
  }
  .card {
    position: absolute;
    left: 197px;
    width: 807px;
    height: 463px;
    border-radius: 20px;
    overflow: hidden;
    background: var(--card-black);
    box-shadow: 0 4px 14px rgba(0,0,0,.25);
  }
  .card--front { top: 127px; }
  .card--back { top: 662px; }
  .card-wave { position: absolute; inset: 0; width: 100%; height: 100%; }

  .person { position: absolute; top: 34px; }
  .card--front .person { right: 38px; text-align: right; }
  .card--back .person { left: 40px; text-align: left; top: 44px; }
  .person-name { font-weight: 700; font-size: 22px; letter-spacing: .5px; }
  .person-title { font-size: 17px; margin-top: 2px; }
  .card--front .person-name { color: var(--brand-gold); }
  .card--front .person-title { color: var(--brand-green); }
  .card--back .person-name { color: var(--brand-green); }
  .card--back .person-title { color: #a79d83; }

  .brand-name {
    position: absolute;
    font-family: "Montserrat", Arial, sans-serif;
    font-weight: 800;
    color: var(--brand-green);
    text-transform: uppercase;
    line-height: 1;
    white-space: nowrap;
  }
  .card--front .brand-name { left: 0; right: 0; top: 170px; text-align: center; }
  .card--front .brand-main { font-size: 68px; letter-spacing: 6px; display: block; }
  .card--front .brand-sub { font-size: 22px; letter-spacing: 7px; display: block; margin-top: 12px; }
  .card--back .brand-name {
    left: 0; right: 0; top: 205px;
    display: flex; align-items: center; justify-content: center; gap: 20px;
  }
  .card--back .brand-main { font-size: 50px; letter-spacing: 4px; }
  .card--back .brand-sub { font-size: 18px; letter-spacing: 5px; line-height: 1.35; }

  .contact-row {
    position: absolute;
    left: 0; right: 0; top: 388px;
    font-size: 18px;
    line-height: 27px;
  }
  .card--front .contact-row { color: var(--ink-dark); }
  .card--back .contact-row { color: var(--brand-gold); top: 391px; }
  .contact-item { position: absolute; display: flex; gap: 14px; }
  .contact-item--address { left: 38px; }
  .contact-item--phone { left: 306px; }
  .contact-item--online { left: 522px; }
  .contact-icons { display: flex; flex-direction: column; }
  .contact-icons svg { width: 16px; height: 16px; margin: 5px 0 6px; fill: currentColor; }
  .web-address { letter-spacing: 3px; }

  .side-label {
    position: absolute;
    width: 182px; height: 182px;
    border-radius: 50%;
    border: 9px solid var(--label-ring);
    background: var(--label-fill);
    display: flex; align-items: center; justify-content: center;
    font-size: 46px;
    color: #111;
    z-index: 2;
  }
  .side-label--front { left: 6px; top: 14px; }
  .side-label--back { left: 975px; top: 596px; }
</style>
</head>
<body>

<div class="side-label side-label--front">FRONT</div>

<section class="card card--front">
  <svg class="card-wave" viewBox="0 0 807 463" preserveAspectRatio="none" aria-hidden="true">
    <defs>
      <linearGradient id="gold-band" x1="0" y1="0" x2="1" y2="0">
        <stop offset="0" stop-color="var(--gold-deep)"/>
        <stop offset=".45" stop-color="var(--gold-light)"/>
        <stop offset="1" stop-color="var(--gold-deep)"/>
      </linearGradient>
    </defs>
    <path d="M0 330 C180 345 320 372 450 362 C580 352 680 340 807 352 L807 463 L0 463 Z" fill="url(#gold-band)"/>
  </svg>

  <div class="person">
    <p class="person-name">DANA WHITFIELD</p>
    <p class="person-title">Director of Software Development</p>
  </div>

  <h1 class="brand-name">
    <span class="brand-main">Northgate</span>
    <span class="brand-sub">Trade Corporation</span>
  </h1>

  <div class="contact-row">
    <div class="contact-item contact-item--address">
      <div class="contact-icons"><svg viewBox="0 0 16 16"><path d="M8 0a5.5 5.5 0 0 0-5.5 5.5C2.5 10 8 16 8 16s5.5-6 5.5-10.5A5.5 5.5 0 0 0 8 0zm0 8a2.5 2.5 0 1 1 0-5 2.5 2.5 0 0 1 0 5z"/></svg></div>
      <p>418 Harbor View Lane<br>Bayport, AL 36512</p>
    </div>
    <div class="contact-item contact-item--phone">
      <div class="contact-icons">
        <svg viewBox="0 0 16 16"><path d="M1 6c0-3 3-4 7-4s7 1 7 4l-3 1-1-2H5L4 7 1 6zm3 2h8l2 6H2l2-6zm4 1.5a2 2 0 1 0 0 4 2 2 0 0 0 0-4z"/></svg>
        <svg viewBox="0 0 16 16"><path d="M4 0h8a1 1 0 0 1 1 1v14a1 1 0 0 1-1 1H4a1 1 0 0 1-1-1V1a1 1 0 0 1 1-1zm1 2v10h6V2H5zm3 11a1 1 0 1 0 0 2 1 1 0 0 0 0-2z"/></svg>
      </div>
      <p>555.014.2270<br>555.014.2270</p>
    </div>
    <div class="contact-item contact-item--online">
      <div class="contact-icons">
        <svg viewBox="0 0 16 16"><path d="M0 3h16v10H0V3zm1.5 1.2L8 9l6.5-4.8V4h-13v.2z"/></svg>
        <svg viewBox="0 0 16 16"><path d="M8 0a8 8 0 1 0 0 16A8 8 0 0 0 8 0zm-1 2v3H3.5A6 6 0 0 1 7 2zm2 0a6 6 0 0 1 3.5 3H9V2zM2.3 7H7v2H2.3a6 6 0 0 1 0-2zM9 7h4.7a6 6 0 0 1 0 2H9V7zm-5.5 4H7v3a6 6 0 0 1-3.5-3zM9 11h3.5A6 6 0 0 1 9 14v-3z"/></svg>
      </div>
      <p>dwhitfield@northgatetc.com<br><span class="web-address">www.northgatetc.com</span></p>
    </div>
  </div>
</section>

<div class="side-label side-label--back">BACK</div>

<section class="card card--back">
  <svg class="card-wave" viewBox="0 0 807 463" preserveAspectRatio="none" aria-hidden="true">
    <defs>
      <radialGradient id="green-band" cx=".6" cy="1" r=".8">
        <stop offset="0" stop-color="var(--brand-green)"/>
        <stop offset="1" stop-color="var(--brand-green-dark)"/>
      </radialGradient>
    </defs>
    <path d="M0 326 C160 372 330 372 480 358 C620 345 720 328 807 334 L807 463 L0 463 Z" fill="url(#green-band)"/>
  </svg>

  <div class="person">
    <p class="person-name">DANA WHITFIELD</p>
    <p class="person-title">Director of Consulting Development</p>
  </div>

  <h2 class="brand-name">
    <span class="brand-main">Northgate</span>
    <span class="brand-sub">Trade<br>Corporation</span>
  </h2>

  <div class="contact-row">
    <div class="contact-item contact-item--address">
      <div class="contact-icons"><svg viewBox="0 0 16 16"><path d="M8 0a5.5 5.5 0 0 0-5.5 5.5C2.5 10 8 16 8 16s5.5-6 5.5-10.5A5.5 5.5 0 0 0 8 0zm0 8a2.5 2.5 0 1 1 0-5 2.5 2.5 0 0 1 0 5z"/></svg></div>
      <p>418 Harbor View Lane<br>Bayport, AL 36512</p>
    </div>
    <div class="contact-item contact-item--phone">
      <div class="contact-icons">
        <svg viewBox="0 0 16 16"><path d="M1 6c0-3 3-4 7-4s7 1 7 4l-3 1-1-2H5L4 7 1 6zm3 2h8l2 6H2l2-6zm4 1.5a2 2 0 1 0 0 4 2 2 0 0 0 0-4z"/></svg>
        <svg viewBox="0 0 16 16"><path d="M4 0h8a1 1 0 0 1 1 1v14a1 1 0 0 1-1 1H4a1 1 0 0 1-1-1V1a1 1 0 0 1 1-1zm1 2v10h6V2H5zm3 11a1 1 0 1 0 0 2 1 1 0 0 0 0-2z"/></svg>
      </div>
      <p>555.014.2270<br>555.014.2270</p>
    </div>
    <div class="contact-item contact-item--online">
      <div class="contact-icons">
        <svg viewBox="0 0 16 16"><path d="M0 3h16v10H0V3zm1.5 1.2L8 9l6.5-4.8V4h-13v.2z"/></svg>
        <svg viewBox="0 0 16 16"><path d="M8 0a8 8 0 1 0 0 16A8 8 0 0 0 8 0zm-1 2v3H3.5A6 6 0 0 1 7 2zm2 0a6 6 0 0 1 3.5 3H9V2zM2.3 7H7v2H2.3a6 6 0 0 1 0-2zM9 7h4.7a6 6 0 0 1 0 2H9V7zm-5.5 4H7v3a6 6 0 0 1-3.5-3zM9 11h3.5A6 6 0 0 1 9 14v-3z"/></svg>
      </div>
      <p>dwhitfield@northgatetc.com<br><span class="web-address">www.northgatetc.com</span></p>
    </div>
  </div>
</section>

</body>
</html>
```